bright harbour vehicle graphics

Hi designers.
We are looking for some designs for our two new work cars.
They are:
- Korvel Tessin duel cab tray back 4x4
- White in colour
What we want to see on the car:
- an interesting modern eye catching design.
- company name : bright harbour landscapes
- company vine ( see atachment)
- name : Oliver pickett, this will be on one car and the other car will have the name: james tollisch.
- website: www.bhlandscapes-example.com.au
- Lic 815904k
- words : design, construct, maintain somewhere
- colours green, black greyscale but open to ideas.
Budget:
we have a budget of about $1300 per car for the installation cost of putting the stickers on.
I will attach some files soon of the vine as mentioned as well as some other usefull images that be helpfull.
also happy to see some other graphics as well.
Thanks designers.
good luck
Reason: I want to see more designs before i decide. This is going to be on the cars for a long time and i want it to be great.

```html
<!DOCTYPE html>
<html lang="en">
<head>
<meta charset="utf-8">
<title>Bright Harbour Landscapes – Vehicle Graphic</title>
<link rel="stylesheet" href="https://fonts.googleapis.com/css2?family=Ubuntu:wght@300;400&display=swap">
<style>
  :root {
    --leaf-green: #8dc63f;
    --panel-black: #0d0d0d;
    --panel-grey: #2a2a2a;
    --type-white: #ffffff;
    --page: #ffffff;
  }
  html, body {
    margin: 0;
    padding: 0;
    width: 1200px;
    height: 571px;
    overflow: hidden;
    background: var(--page);
  }
  .vehicle-graphic {
    display: block;
    width: 1200px;
    height: 571px;
    font-family: "Ubuntu", Arial, sans-serif;
  }
  .border-swoosh { fill: var(--leaf-green); }
  .panel { fill: url(#panelShade); }
  .driver-name { fill: var(--type-white); font-size: 31px; font-weight: 400; }
  .company-name { fill: var(--type-white); font-weight: 400; }
  .company-name__main { font-size: 50px; letter-spacing: 3px; }
  .company-name__sub { font-size: 29px; letter-spacing: 13px; }
  .services { fill: var(--type-white); font-size: 29px; font-weight: 400; }
  .website { fill: var(--type-white); font-size: 37px; font-weight: 300; }
  .website__domain { fill: var(--leaf-green); }
  .licence { fill: var(--type-white); font-size: 21px; font-weight: 400; letter-spacing: 1px; }
</style>
</head>
<body>
<svg class="vehicle-graphic" viewBox="0 0 1200 571" xmlns="http://www.w3.org/2000/svg">
  <defs>
    <radialGradient id="panelShade" cx="0.42" cy="0.5" r="0.65">
      <stop offset="0" stop-color="var(--panel-grey)"/>
      <stop offset="1" stop-color="var(--panel-black)"/>
    </radialGradient>
    <radialGradient id="vineTones" cx="0.65" cy="0.6" r="0.6">
      <stop offset="0" stop-color="#a9d86a" stop-opacity="0.55"/>
      <stop offset="0.5" stop-color="#d9e8c4" stop-opacity="0.3"/>
      <stop offset="1" stop-color="#8dc63f" stop-opacity="0"/>
    </radialGradient>
  </defs>

  <path class="border-swoosh" d="M1120,110 C900,84 400,80 180,170 C70,215 55,290 110,350 C150,395 200,435 240,458 L1120,458 Z"/>
  <path class="panel" d="M1120,122 C900,98 420,95 210,178 C105,222 95,290 140,350 C178,395 220,430 256,458 L1120,458 Z"/>

  <rect class="vine-decoration" x="850" y="150" width="270" height="308"
        fill="url(#vineTones)" role="img"
        aria-label="Company vine: curling green and white leafy tendrils rising from the lower right corner"/>

  <text class="driver-name" x="775" y="165">Oliver Pickett</text>

  <g class="company-name">
    <text class="company-name__main" x="258" y="242">BRIGHT HARBOUR</text>
    <text class="company-name__sub" x="262" y="292">Landscapes</text>
  </g>

  <text class="services" x="260" y="352">DESIGN . CONSTRUCTION . MAINTAIN</text>

  <text class="website" x="256" y="422">www.<tspan class="website__domain">bhlandscapes-example</tspan>.net</text>

  <text class="licence" transform="translate(186 368) rotate(-90)">Lic 815904k</text>
</svg>
</body>
</html>
```